Lumo Academics - new College Consulting company in San Francisco needs a flyer design

We need a logo design for a new college admissions consulting business in San Francisco Bay Area and San Jose called 'Lumo Academics'. We plan to develop tailor-made strategies for each students dreams and aspirations and will help provide them with online classes and in-person consulting starting Summer 2022.
Lumo Academics plans on providing a free first time consulting to attract clients and grow our client base from there.
Lumo Academics has a small team of consultants who have degrees from Economics/Business, Biology, and Computer Science who can provide tailored guidance to meet student and parent expectations and spend the time to walk them throughout the process.
Please refer to attached logos for the company and to create a flyer.
Competitive College Consulting
Education Consulting

```html
<!DOCTYPE html>
<html lang="en">
<head>
<meta charset="utf-8">
<title>Lumo Academics Flyer</title>
<link rel="stylesheet" href="https://fonts.googleapis.com/css2?family=Montserrat:wght@400;500;600;700&family=Oswald:wght@400;500&family=Playball&family=Lora&display=swap">
<style>
  :root {
    --coral: #f78f86;
    --coral-deep: #e8716a;
    --ink: #333336;
    --text: #4a4a4d;
    --panel: #f1f1f1;
    --rule: #c9c9c9;
    --bar-dark: #2b2b2b;
    --bar-grey: #6a6a6c;
    --white: #ffffff;
  }
  * { margin: 0; padding: 0; box-sizing: border-box; }
  html, body { width: 800px; height: 1200px; overflow: hidden; background: var(--white); }
  body { font-family: "Montserrat", sans-serif; color: var(--text); }
  .flyer { position: relative; width: 800px; height: 1200px; overflow: hidden; background: var(--white); }
  .abs { position: absolute; }

  .hero-photo {
    left: 0; top: 0; width: 423px; height: 405px;
    background: linear-gradient(135deg, #d9c8bd 0%, #b88e78 40%, #7c5b4d 70%, #c9c4c2 100%);
  }
  .class-photo {
    left: 62px; top: 857px; width: 305px; height: 226px;
    background: linear-gradient(120deg, #e4e1dc 0%, #b4a394 45%, #8d6f62 70%, #c23a3e 100%);
  }
  .shapes { left: 0; top: 0; width: 800px; height: 1200px; }

  .brand { right: 40px; top: 42px; display: flex; align-items: center; gap: 14px; text-align: right; }
  .brand-name { font-family: "Montserrat", sans-serif; font-weight: 600; font-size: 22px; color: var(--ink); line-height: 1.1; }
  .brand-tagline { font-family: "Lora", serif; font-size: 18px; color: var(--ink); margin-top: 2px; }
  .brand-mark { width: 34px; height: 34px; border-radius: 50%; background: var(--ink); }

  .intro { left: 440px; top: 152px; width: 324px; text-align: right; }
  .intro-kicker { font-family: "Playball", cursive; font-size: 32px; color: var(--coral-deep); line-height: 1; }
  .intro-title { font-weight: 700; font-size: 37px; line-height: 1.05; color: var(--ink); margin-top: 4px; }
  .intro-title-line { display: block; width: 58px; height: 4px; background: var(--coral); margin: 6px 0 0 auto; }
  .intro-text { font-size: 12.5px; line-height: 1.3; color: var(--ink); margin-top: 18px; }

  .date-badge { left: 56px; top: 281px; width: 266px; height: 266px; display: flex; flex-direction: column; align-items: center; justify-content: center; color: var(--white); text-align: center; }
  .date-day, .date-full { font-family: "Oswald", sans-serif; font-weight: 500; font-size: 38px; line-height: 1.05; }
  .date-time { font-family: "Oswald", sans-serif; font-weight: 400; font-size: 23px; margin-top: 8px; padding: 0 6px 2px; border-top: 2px solid rgba(255,255,255,.85); border-bottom: 2px solid rgba(255,255,255,.85); line-height: 1.3; }

  .section-title { font-weight: 600; font-size: 19px; line-height: 1.2; color: var(--ink); margin-bottom: 8px; }
  .body-copy { font-size: 11.6px; line-height: 16.5px; text-align: justify; color: var(--text); }
  .body-copy + .body-copy { margin-top: 20px; }

  .left-column { left: 62px; top: 580px; width: 305px; }

  .side-panel { left: 423px; top: 427px; width: 322px; height: 662px; background: var(--panel); padding: 26px 27px 0 29px; }
  .side-panel .body-copy + .body-copy { margin-top: 20px; }
  .panel-rule { height: 1px; background: var(--rule); margin: 26px 0 24px; }

  .call { left: 64px; top: 1112px; color: var(--white); }
  .call-label { font-weight: 600; font-size: 21px; line-height: 1; }
  .call-number { font-weight: 700; font-size: 40px; line-height: 1.1; letter-spacing: 1px; }

  .contact { left: 440px; top: 1110px; font-style: normal; }
  .contact-row { display: flex; align-items: center; gap: 12px; font-weight: 500; font-size: 20px; color: var(--ink); height: 34px; }
  .contact-row svg { width: 17px; height: 17px; flex: none; }
</style>
</head>
<body>
<main class="flyer">
  <div class="abs hero-photo" role="img" aria-label="Photo of three smiling students gathered around a laptop"></div>
  <div class="abs class-photo" role="img" aria-label="Photo of students studying together at a laptop in a bright classroom"></div>

  <svg class="abs shapes" viewBox="0 0 800 1200" aria-hidden="true">
    <polygon points="320,0 800,0 800,133 378,133" fill="var(--coral)"/>
    <rect x="423" y="133" width="377" height="272" fill="var(--white)"/>
    <polygon points="0,405 345,405 333,427 0,427" fill="var(--bar-dark)"/>
    <polygon points="350,405 800,405 800,418 343,418" fill="var(--coral)"/>
    <polygon points="0,1103 385,1103 433,1200 0,1200" fill="var(--coral)"/>
    <rect x="433" y="1190" width="367" height="10" fill="var(--bar-grey)"/>
    <g transform="translate(189 414) rotate(45)">
      <rect x="-92" y="-92" width="188" height="188" rx="14" fill="var(--coral-deep)" opacity=".35"/>
      <rect x="-94" y="-94" width="188" height="188" rx="14" fill="var(--coral)"/>
    </g>
  </svg>

  <header class="abs brand">
    <div>
      <div class="brand-name">Lumo Academics</div>
      <div class="brand-tagline">Learning is a phenomenom</div>
    </div>
    <span class="brand-mark"></span>
  </header>

  <section class="abs intro">
    <div class="intro-kicker">Lumo Academics</div>
    <h1 class="intro-title">Learning is a<br>Phenomenom</h1>
    <span class="intro-title-line"></span>
    <p class="intro-text">We plan to develop tailor-made strategies for each students dreams and aspirations and will help provide them with online classes and in-person consulting starting Summer 2022.</p>
  </section>

  <div class="abs date-badge">
    <div class="date-day">SUNDAY</div>
    <div class="date-full">MAY 31, 2022</div>
    <div class="date-time">4PM-5PM</div>
  </div>

  <section class="abs left-column">
    <h2 class="section-title">Lorem Ipsum</h2>
    <p class="body-copy">Lorem Ipsum is simply dummy text of the printing and typesetting industry. Lorem Ipsum has been the industry's standard dummy text ever since the 1500s, when an unknown printer took a galley of type and scrambled it to make a type specimen book.</p>
    <p class="body-copy">Lorem Ipsum is simply dummy text of the printing and typesetting industry. Lorem Ipsum has been the industry's standard dummy text ever since the 1500s, when an unknown printer took a galley of type and scrambled it to make a type specimen book.</p>
  </section>

  <aside class="abs side-panel">
    <h2 class="section-title">Lorem Ipsum</h2>
    <p class="body-copy">Lorem Ipsum is simply dummy text of the printing and typesetting industry. Lorem Ipsum has been the industry's standard dummy text ever since the 1500s, when an unknown printer took a galley of type and scrambled it to make a type specimen book.</p>
    <p class="body-copy">Lorem Ipsum is simply dummy text of the printing and typesetting industry. Lorem Ipsum has been the industry's standard dummy text ever since the 1500s, when an unknown printer took a galley of type and scrambled it to make a type specimen book.</p>
    <p class="body-copy">Lorem Ipsum is simply dummy text of the printing and typesetting industry. Lorem Ipsum has been the industry's standard dummy text ever since the 1500s, when an unknown printer took a galley of type and scrambled it to make a type specimen book.</p>
    <div class="panel-rule"></div>
    <h2 class="section-title">Lorem Ipsum</h2>
    <p class="body-copy">Lorem Ipsum is simply dummy text of the printing and typesetting industry. Lorem Ipsum has been the industry's standard dummy text ever since the 1500s, when an unknown printer took a galley of type and scrambled it to make a type specimen book.</p>
  </aside>

  <div class="abs call">
    <div class="call-label">Call us now!</div>
    <div class="call-number">555 014 2290</div>
  </div>

  <address class="abs contact">
    <div class="contact-row">
      <svg viewBox="0 0 20 20"><rect x="1" y="4" width="18" height="12" rx="1.5" fill="var(--coral)"/><polyline points="2,5 10,11 18,5" fill="none" stroke="var(--white)" stroke-width="1.6"/></svg>
      <span>hello@lumoacademics.com</span>
    </div>
    <div class="contact-row">
      <svg viewBox="0 0 20 20" fill="none" stroke="var(--coral)" stroke-width="1.6"><circle cx="10" cy="10" r="8.2"/><ellipse cx="10" cy="10" rx="3.6" ry="8.2"/><line x1="2" y1="10" x2="18" y2="10"/><line x1="3.5" y1="5.5" x2="16.5" y2="5.5"/><line x1="3.5" y1="14.5" x2="16.5" y2="14.5"/></svg>
      <span>www.lumoacademics.com</span>
    </div>
  </address>
</main>
</body>
</html>
```